Driving-coach/trainer who wants to inform about the offer and how I can help people to drive more re

I need a flyer that informs potential customers about my offer.

DL size 210 mm x 99 mm, vertical!

I'm a trainer/coach who helps people to drive a car more relaxed, without fear and more confident.

It's a one to one training. I do train people in their own car. It gets people their freedom back to go where and when they like to go by own car...

Target Market(s)

People (man an woman) who are afraid of driving a car, or are very stressed while driving....

Industry/Entity Type

Life Coaching

Font styles to use
Sans Serif

Colors
acd136

Requirements
Must have
• Page 1:
• -my offer (see text-pdf)
• -three fotos (see attached files "Pixmarra") of people who are satisfied with my offer
• Page 2:
• -advantages in the work with me.
• -contact information
• -and a picture of me (see attached file) next to the contact information or the advantages of my work
• -my logo (see attached file) on Page 1 + 2
• -i like a "clear" and structured layout. "Less is more"

```html
<!DOCTYPE html>
<html lang="de">
<head>
<meta charset="utf-8">
<title>Fahrangst erfolgreich loswerden – Flyer</title>
<link href="https://fonts.googleapis.com/css2?family=Passion+One:wght@400;700&family=Montserrat:wght@400;500;700&family=Exo+2:wght@400;500&display=swap" rel="stylesheet">
<style>
  :root{
    --green-dark:#1f5b3b;
    --green:#5aab3f;
    --green-light:#6fbf4a;
    --lime:#acd136;
    --cream:#f4f5e6;
    --sky:#a9c9dc;
    --text:#3d3d3d;
    --white:#ffffff;
  }
  *{box-sizing:border-box;margin:0;padding:0}
  html,body{width:1183px;height:1200px;overflow:hidden;background:var(--white)}
  body{position:relative;font-family:"Montserrat",sans-serif;color:var(--text)}
  .panel{position:absolute;top:0;height:1200px;width:576px;overflow:hidden;
    background:linear-gradient(180deg,#9fc3d8 0%,#d8e7ee 22%,#f3f6f2 45%,var(--cream) 100%)}
  .panel--front{left:0;width:575px}
  .panel--back{left:607px}
  .abs{position:absolute}
  .display{font-family:"Passion One",sans-serif;line-height:.9;text-transform:lowercase}

  /* front */
  .hero-title{left:0;width:575px;text-align:center;color:var(--green-dark);
    text-shadow:0 0 6px rgba(255,255,255,.8)}
  .hero-title .l1{top:38px;font-size:96px}
  .hero-title .l2{top:125px;font-size:70px;transform:rotate(-4deg)}
  .hero-title .l3{top:178px;font-size:110px;transform:rotate(-4deg);text-transform:none}
  .hero-photo{left:0;top:250px;width:575px;height:250px;
    background:linear-gradient(180deg,#c8dbe4 0%,#6f8f52 28%,#c9a46a 55%,#e2d23a 75%,#8aa84b 100%)}
  .circle-photo{border-radius:50%;border:4px solid var(--white);box-shadow:0 3px 10px rgba(0,0,0,.3)}
  .circle-photo--a{left:162px;top:494px;width:152px;height:152px;background:radial-gradient(circle at 60% 40%,#e8c9a8,#8a6b4c 70%,#3a3a3a)}
  .circle-photo--b{left:308px;top:556px;width:232px;height:232px;background:radial-gradient(circle at 45% 40%,#f0d2a8,#d8b98a 40%,#c9d2d6 75%,#8b949a)}
  .wollen{left:36px;top:626px;font-size:35px;color:var(--green)}
  .wollen span{color:var(--green-dark)}
  .checks{left:36px;top:676px;list-style:none;font-size:19px;line-height:24px;color:var(--text)}
  .checks li{position:relative;padding-left:31px;margin-bottom:10px}
  .checks li::before{content:"";position:absolute;left:2px;top:5px;width:7px;height:13px;border:solid var(--green);border-width:0 3px 3px 0;transform:rotate(40deg)}
  .checks b{color:var(--green)}
  .richtig{left:36px;top:836px;font-size:40px;color:var(--green-dark);transform:rotate(-2deg);transform-origin:left}
  .question{left:36px;top:888px;font-size:18.5px;font-weight:700;color:var(--green)}
  .situations{left:36px;top:926px;width:510px;list-style:none;font-size:14.4px;line-height:20.8px}
  .situations li{position:relative;padding-left:19px;margin-bottom:8px}
  .situations li::before,.advantages li::before{content:"";position:absolute;left:0;top:4px;width:4px;height:13px;background:var(--green)}
  .situations b{color:#333}
  .hl{color:var(--green)}

  /* back */
  .claim{left:0;width:576px;text-align:center}
  .claim .c1{top:36px;font-size:78px;color:var(--green-dark);transform:rotate(-3deg)}
  .claim .c2{top:110px;font-size:80px;color:var(--green);transform:rotate(-3deg)}
  .steps-label{left:38px;top:232px;font-size:24px;font-weight:700;color:var(--green-dark);line-height:25px}
  .step{border-radius:50%;border:4px solid var(--white);display:flex;flex-direction:column;align-items:center;justify-content:center;text-align:center;box-shadow:0 3px 10px rgba(0,0,0,.25)}
  .step--1{left:215px;top:186px;width:142px;height:142px;background:var(--green-light);color:var(--green-dark);font-size:17px;line-height:20px}
  .step--2{left:337px;top:216px;width:200px;height:200px;background:var(--green-light);color:var(--green-dark);font-size:18.5px;line-height:27px}
  .step--3{left:136px;top:296px;width:252px;height:252px;background:var(--green-dark);color:var(--white);font-size:20px;line-height:28px;padding:0 18px}
  .step--3 small{font-size:12px;line-height:17px;margin-top:2px}
  .advantages{left:38px;top:568px;width:512px;list-style:none;font-size:15px;line-height:21.6px;color:var(--green-dark)}
  .advantages li{position:relative;padding-left:20px;margin-bottom:8px}
  .advantages li::before{top:5px}
  .advantages u{color:var(--green)}
  .portrait{left:412px;top:898px;width:164px;height:302px;border-radius:82px 82px 0 0;
    background:linear-gradient(180deg,#8a7565 0%,#d9b9a0 30%,#f4f4f4 55%,#e6e9ea 100%)}
  .contact-name{left:40px;top:938px;z-index:2;color:var(--white);font-family:"Exo 2",sans-serif;letter-spacing:2px}
  .contact-name .name{font-size:26px;line-height:30px}
  .contact-name .role{font-size:19px;line-height:24px;letter-spacing:1.4px}
  .info{left:38px;top:1039px;font-size:13.5px;line-height:17px;color:#333}
  .web{left:38px;top:1078px;font-size:21px;color:var(--green-dark)}
  .call{left:38px;top:1114px;font-size:16px;color:#444;letter-spacing:-.2px}
  .phone{left:38px;top:1134px;font-size:31px;font-weight:700;color:var(--green-dark);letter-spacing:.5px}
</style>
</head>
<body>

<section class="panel panel--front">
  <div class="hero-photo abs" role="img" aria-label="Foto: gelber Kleinwagen mit Koffern auf dem Dach in einem Kornfeld, fröhliche Fahrerin winkt"></div>
  <svg class="abs" style="left:0;top:0" width="575" height="1200" viewBox="0 0 575 1200" aria-hidden="true">
    <path d="M0,390 C120,470 300,500 575,470 L575,1200 L0,1200 Z" fill="var(--green)"/>
    <path d="M0,420 C140,500 330,520 575,490 L575,1200 L0,1200 Z" fill="var(--green-light)" opacity=".55"/>
    <path d="M0,470 C150,520 330,520 575,455 L575,520 C380,560 180,560 0,540 Z" fill="var(--green-dark)" opacity=".85"/>
    <path d="M0,600 C80,565 200,545 320,560 C400,700 540,760 575,880 L575,1200 L0,1200 Z" fill="var(--green-dark)"/>
    <path d="M0,612 C90,578 210,560 318,574 C395,712 530,772 562,890 L562,1200 L0,1200 Z" fill="var(--cream)"/>
  </svg>
  <div class="hero-title display">
    <div class="abs l1" style="left:0;width:575px">fahrangst</div>
    <div class="abs l2" style="left:0;width:575px">erfolgreich</div>
    <div class="abs l3" style="left:0;width:575px">Loswerden</div>
  </div>
  <div class="circle-photo circle-photo--a abs" role="img" aria-label="Foto: lächelnde Frau am Steuer eines Cabrios"></div>
  <div class="circle-photo circle-photo--b abs" role="img" aria-label="Foto: junge Frau lehnt aus dem Autofenster und zeigt Daumen hoch"></div>

  <h2 class="wollen abs display">wollen <span>sie:</span></h2>
  <ul class="checks abs">
    <li>Fahrangst überwinden<b>?</b></li>
    <li>Panikattacken beim<br>Autofahren loswerden<b>?</b></li>
    <li>Oder einfach sicher<br>Autofahren<b>?</b></li>
  </ul>
  <h2 class="richtig abs display">dann sind sie hier richtig!</h2>
  <p class="question abs">Kommt Ihnen eine dieser Situationen bekannt vor?</p>
  <ul class="situations abs">
    <li><b>Angst oder Panikattacken</b> begleiten Sie <b>beim Autofahren.</b> Vielleicht vermeiden Sie deshalb das Autofahren komplett. - Sie möchten <span class="hl">angstfreiund/oder ohne Panikattacken fahren.</span></li>
    <li>Sie <b>trauen sich das Autofahren nicht (mehr) zu.</b> - Sie wünschen sich, <span class="hl">sicher, entspannt und stressfrei</span> Auto zu fahren.</li>
    <li><b>Autofahren</b> erleben Sie unter <b>hoher Anspannung und Stress.</b> - Sie wünschen sich, Autofahren <span class="hl">sicher und entspannt</span> zu erleben.</li>
    <li>Bestimmte Situationen (z.B. <b>Autobahn, Baustellen, Stadtvekehr...)</b> bereiten Ihnen <b>großen Stress.</b> - Sie möchten diese Situationen <span class="hl">souveräner</span> meistern.</li>
  </ul>
</section>

<section class="panel panel--back">
  <svg class="abs" style="left:0;top:0" width="576" height="1200" viewBox="0 0 576 1200" aria-hidden="true">
    <path d="M0,850 C120,905 360,920 576,840 L576,1200 L0,1200 Z" fill="var(--green-dark)"/>
    <path d="M0,875 C140,925 380,930 576,870 L576,1200 L0,1200 Z" fill="var(--green)"/>
    <path d="M0,1010 C120,995 280,1000 400,1060 L576,1090 L576,1200 L0,1200 Z" fill="var(--green-dark)"/>
    <path d="M0,1022 C130,1008 290,1014 410,1074 L576,1104 L576,1200 L0,1200 Z" fill="var(--cream)"/>
  </svg>
  <div class="claim display">
    <div class="abs c1" style="left:0;width:576px">das muss nicht</div>
    <div class="abs c2" style="left:0;width:576px">so bleiben!</div>
  </div>
  <p class="steps-label abs">3 Schritte<br>zur Lösung:</p>
  <div class="step step--1 abs">Erstgespräch<br>vereinbaren</div>
  <div class="step step--2 abs">Analyse Ihrer<br>individuellen<br>Situation und<br>Zielsetzung</div>
  <div class="step step--3 abs">Individuelles<br>Coaching und<br>Training
    <small>(ggf. Fahrangst-Therapie - als<br>psychotherapeutische<br>Heilpraktikerin<br>bin ich auf Angst- und<br>Panikstörungen<br>spezialisiert)</small></div>

  <ul class="advantages abs">
    <li>über 10 Jahre Erfahrung als <span class="hl">Trainerin</span> und Coach im Bereich <span class="hl">Fahrsicherheit.</span></li>
    <li>Als <span class="hl">psychotherapeutische Heilpraktikerin</span> bin ich <span class="hl">auf Angststörungen und Panikattacken spezialisiert</span></li>
    <li><span class="hl">100 % auf Sie zugeschnitten:</span> ich hole Sie genau dort ab, wo Sie jetzt stehen und unterstütze Sie in <span class="hl">Ihrem Prozess individuell und zielführend.</span></li>
    <li>Wenn es Ihnen nicht möglich ist, in meine Praxis nach Grünwalde Nord zu kommen: <u>Mit der mobilen</u> <span class="hl">Praxis komme ich auch zu Ihnen.</span></li>
    <li><span class="hl">Termine</span> sind auch <span class="hl">abends und am Wochenende möglich.</span></li>
  </ul>

  <div class="portrait abs" role="img" aria-label="Porträtfoto der Trainerin in weißer Bluse"></div>
  <div class="contact-name abs">
    <div class="name">Katrin Lindholm</div>
    <div class="role">Fahrangst-Bewältigungs-Coach</div>
  </div>
  <p class="info abs">Weitere Informationen<br>finden Sie auf:</p>
  <p class="web abs">sicher-ankommen-coaching.de</p>
  <p class="call abs">Oder rufen Sie mich einfach an:</p>
  <p class="phone abs">0151 23 48 61 90</p>
</section>

</body>
</html>
```